teaching love. a joyful state of being.

adding value to ones circumstance through the teachings of neutralization. quote for back of card: "and then it happens... One day you wake up and you're in this place. You are in this place where everything is right. Your heart is calm. Your soul is lit. Your thoughts are positive. Your vision is clear. Your faith is stronger than ever. And you are at peace. At peace with where you have been. At peace with what you've been through. And at peace with where you're headed." -unknown

Target Market(s)

spiritual, awakening, inspiration, motivation, gratefulness, oneness, peace, positive mindset,

Contact Information for Business Card

front: one line message from quote

Logo Text

up to suggestions

Font styles to use
Serif
Sans Serif
Script

Colors

Designer to choose colors to be used in the design.

Requirements
Must have
• entire quote on one side of card
Nice to have
• simple, and to the point
Should not have
• elaborated designs

```html
<!DOCTYPE html>
<html lang="en">
<head>
<meta charset="utf-8">
<title>Still Water — Business Card</title>
<link rel="stylesheet" href="https://fonts.googleapis.com/css2?family=Nunito+Sans:wght@300;400;600&display=swap">
<style>
  :root {
    --bg: #1c1c1e;
    --navy-deep: #1c1d6e;
    --navy: #1f2a86;
    --blue-mid: #1f4e96;
    --ink: #1d2250;
    --ink-soft: #2a2f5e;
    --white: #ffffff;
    --gold: #e6b724;
    --mist: #eceef6;
    --mist-blue: rgba(140, 160, 220, 0.18);
  }
  * { box-sizing: border-box; margin: 0; padding: 0; }
  html, body { width: 1200px; height: 900px; overflow: hidden; }
  body {
    background: var(--bg);
    font-family: "Nunito Sans", "Helvetica Neue", Arial, sans-serif;
    position: relative;
  }
  .card {
    position: absolute;
    width: 560px;
    height: 320px;
    overflow: hidden;
    box-shadow: 0 18px 40px rgba(0,0,0,0.55);
  }

  /* Front */
  .card-front {
    left: 110px; top: 100px;
    background: radial-gradient(circle at 35% 75%, var(--blue-mid) 0%, var(--navy) 45%, var(--navy-deep) 100%);
    color: var(--white);
  }
  .card-front .decor {
    position: absolute; left: 250px; top: 40px;
    width: 230px; height: 200px; border-radius: 50%;
    background: var(--mist-blue);
  }
  .card-front .brand {
    position: absolute; left: 70px; top: 190px;
    display: flex; align-items: center; gap: 14px;
  }
  .card-front .brand-dot {
    width: 46px; height: 46px; border-radius: 50%;
    background: var(--white);
  }
  .card-front .brand-name {
    font-size: 30px; font-weight: 400; letter-spacing: 0.5px;
  }
  .card-front .verse {
    position: absolute; right: 40px; top: 78px;
    text-align: right; font-size: 13px; line-height: 1.45; font-weight: 300;
  }

  /* Back */
  .card-back {
    left: 520px; top: 440px;
    background: var(--white);
    color: var(--ink);
    border-bottom: 6px solid var(--navy);
  }
  .card-back .decor {
    position: absolute; right: -20px; top: -20px;
    width: 250px; height: 230px; border-radius: 50%;
    background: var(--mist);
  }
  .card-back .identity {
    position: absolute; left: 60px; top: 92px; text-align: center;
  }
  .card-back .person-name { font-size: 22px; font-weight: 300; letter-spacing: 0.5px; color: var(--ink); }
  .card-back .person-role { font-size: 16px; color: var(--navy); }
  .card-back .divider {
    position: absolute; left: 262px; top: 40px;
    width: 2px; height: 110px;
    background: linear-gradient(to bottom, transparent, #c8c9d4, transparent);
    box-shadow: 3px 0 6px rgba(0,0,0,0.12);
  }
  .card-back .contacts {
    position: absolute; left: 300px; top: 40px;
    list-style: none; font-size: 15px; line-height: 1.55;
  }
  .card-back .contacts li { display: flex; align-items: center; gap: 10px; }
  .card-back .contacts svg { width: 12px; height: 12px; fill: var(--navy); flex: none; }
  .card-back .quote {
    position: absolute; left: 200px; top: 178px; width: 340px;
    font-size: 9.5px; line-height: 1.4; color: var(--ink-soft);
  }
  .card-back .quote-mark { color: var(--navy); font-weight: 600; font-size: 16px; line-height: 0; }
  .card-back .quote-source { color: var(--navy); margin-top: 3px; margin-left: 20px; }
  .card-back .brand {
    position: absolute; left: 28px; top: 232px;
    display: flex; align-items: center; gap: 10px;
  }
  .card-back .brand-dot { width: 30px; height: 30px; border-radius: 50%; background: var(--gold); }
  .card-back .brand-name { font-size: 20px; color: var(--navy); font-weight: 400; }
</style>
</head>
<body>

<section class="card card-front">
  <div class="decor" role="img" aria-label="Faint brand mark decoration"></div>
  <div class="brand">
    <span class="brand-dot"></span>
    <span class="brand-name">Still Water</span>
  </div>
  <p class="verse">
    Your heart is calm<br>
    Your soul is lit<br>
    Your thoughts are positive<br>
    Your faith is strong<br>
    And you are at peace
  </p>
</section>

<section class="card card-back">
  <div class="decor" role="img" aria-label="Faint brand mark decoration"></div>

  <div class="identity">
    <p class="person-name">YOUR NAME</p>
    <p class="person-role">Position</p>
  </div>

  <div class="divider"></div>

  <ul class="contacts">
    <li><svg viewBox="0 0 24 24"><path d="M6.6 10.8a15 15 0 0 0 6.6 6.6l2.2-2.2a1 1 0 0 1 1-.25 11 11 0 0 0 3.6.57 1 1 0 0 1 1 1V20a1 1 0 0 1-1 1A17 17 0 0 1 3 4a1 1 0 0 1 1-1h3.5a1 1 0 0 1 1 1c0 1.25.2 2.45.57 3.57a1 1 0 0 1-.25 1z"/></svg>000 00 00 00</li>
    <li><svg viewBox="0 0 24 24"><path d="M2 5h20v14H2zm2 2v.5l8 5 8-5V7zm0 3v7h16v-7l-8 5z"/></svg>info@yourlogo.com</li>
    <li><svg viewBox="0 0 24 24"><path d="M12 2a7 7 0 0 0-7 7c0 5 7 13 7 13s7-8 7-13a7 7 0 0 0-7-7zm0 9.5A2.5 2.5 0 1 1 12 6.5a2.5 2.5 0 0 1 0 5z"/></svg>your office address</li>
    <li><svg viewBox="0 0 24 24"><path d="M12 2a10 10 0 1 0 0 20 10 10 0 0 0 0-20zm6.9 9h-3a15 15 0 0 0-1.3-5.6A8 8 0 0 1 18.9 11zM12 4.1c.9 1.2 1.8 3.5 1.9 6.9h-3.8c.1-3.4 1-5.7 1.9-6.9zM9.4 5.4A15 15 0 0 0 8.1 11h-3a8 8 0 0 1 4.3-5.6zM5.1 13h3a15 15 0 0 0 1.3 5.6A8 8 0 0 1 5.1 13zm6.9 6.9c-.9-1.2-1.8-3.5-1.9-6.9h3.8c-.1 3.4-1 5.7-1.9 6.9zm2.6-1.3a15 15 0 0 0 1.3-5.6h3a8 8 0 0 1-4.3 5.6z"/></svg>www.yourlogo.com</li>
  </ul>

  <blockquote class="quote">
    <p><span class="quote-mark">&ldquo;</span> and then it happens...<br>
    One day you wake up and you're in this place.<br>
    You are in this place where everything is right.<br>
    Your heart is calm. Your soul is lit. Your thoughts are positive.<br>
    Your vision is clear. Your faith is stronger than ever. And you are at peace.<br>
    At peace with where you have been. At peace with what you've been through.<br>
    And at peace with where you're headed. <span class="quote-mark">&rdquo;</span></p>
    <p class="quote-source">-unknown-</p>
  </blockquote>

  <div class="brand">
    <span class="brand-dot"></span>
    <span class="brand-name">Still Water</span>
  </div>
</section>

</body>
</html>
```